A corporate website

The target design is for Vellmar Glassworks coporate site which is a major international manufacturers for the finest quality of transparent and colored full lead crystal (more than 30% PbO)

Vellmar Glassworks is the largest producer of crystal in world with 98% of its production exported to more than 120 countries.

Vellmar Glassworks has 4 business lines:
1. Crystal Fashion Components
2. Chandeliers Crystal Parts
3. Lighting Collection and special design
4. Gifts and accessories

The winner bidder(s) would be asked to do more jobs

The corporate website is the official site that represents Vellmar HQ in front of world and it includes the following pages:
1. Home page
2. Facilities:
a. Factories overview
b. Factories image and video gallery
c. Show rooms locator
d. Quality Control
3. Media Center with the following sub pages
a. Press releases (Previous and future press releases)
b. Logos & artwork (Hi res images for Vellmar Glassworks to be used by various worldwide media)
c. Media contacts (contacts of Vellmar’s media division)
4. Careers:
a. Publish opened positions from Pindle hire
b. Capture candidates resumes using Pindle hire form
5. About US

Target Market(s)

Business partners, resellers, end customers, press and employees

Industry/Entity Type

Business

Requirements
Must have
• The design should include a home webpage and an internal page design. The design should fullfill the following requriements:

1. Strictly follow the corporate identity materials guidelines - see attachment
2. Supports multi-language
3. User can change between languages using flags
4. Web surfer can optionally change the default language
5. An integrated live chat push button for ChatBrio
8. Site Header should contain the following information:
a. Logo
b. Slogan
c. Links to site pages
d. Link to the home page
e. Link to the landing page
f. A language option drop box
9. Footers should have:
a. Links to all other 5 websites in a dropbox form
b. Link to privacy statement
c. Link to copyright notice
d. Link to sitemap
e. Newsletter subscription one field form
11. Every sub-site should have a universal customer service section that offer the following services:
a. Links to end user installation manuals
b. Links to products cleaning and maintenance guide
c. Customer complaints center
12. A news sub-section that should contain:
a. Latest product and promotional announcements
b. Corporate news
c. Exhibitions coverage
13. A link to vellmar Worldwide:
a. A database driven interactive map reflecting Vellmar list of agents and distributors worldwide with list of supported products this interactive map could be limited in every sub-site for specific line of product
b. Capture potential resellers and agents
c. Become a partner form

```html
<!DOCTYPE html>
<html lang="en">
<head>
<meta charset="utf-8">
<title>Vellmar Glassworks</title>
<link rel="stylesheet" href="https://fonts.googleapis.com/css2?family=Source+Sans+3:wght@400;600;700&family=Arimo:wght@400;700&display=swap">
<style>
:root{
  --page:#1b2130;
  --page-deep:#141925;
  --panel-dark:#131823;
  --lilac:#a9b4de;
  --lilac-ink:#39425f;
  --head:#c5cde9;
  --text-light:#c2c8d6;
  --muted:#8f97ab;
  --white:#ffffff;
  --ink:#111;
  --bar:#2c3444;
}
*{box-sizing:border-box;margin:0;padding:0}
html,body{width:839px;height:1200px;overflow:hidden}
body{background:radial-gradient(ellipse at 30% 10%,#2a3142 0%,var(--page) 55%,var(--page-deep) 100%);font-family:"Source Sans 3",Arial,sans-serif;color:var(--text-light);position:relative;font-size:11px}
.abs{position:absolute}
a{color:inherit;text-decoration:none}

/* top bar */
.lang{left:286px;top:15px;font-size:10px;color:#d5dae6;display:flex;align-items:center;gap:4px}
.flag{display:inline-block;width:15px;height:10px}
.lang-select{left:343px;top:12px;width:79px;height:20px;background:#11151d;border-radius:3px;display:flex;align-items:center;padding-left:6px;gap:5px;font-size:10px;color:#e4e7ee}
.toplinks{left:453px;top:12px;display:flex;align-items:center;gap:10px;font-size:10px;color:#cdd3e0}
.search{left:595px;top:9px;width:218px;height:26px;background:linear-gradient(#58606c,#454c57);border-radius:3px;display:flex;align-items:center;padding-left:8px;gap:8px;font-size:10px;color:#b6bcc7}

/* brand */
.brand-card{left:48px;top:85px;width:149px;height:105px;border-radius:10px;background:linear-gradient(#ffffff,#dfe2e7);box-shadow:0 8px 18px rgba(0,0,0,.5);display:flex;flex-direction:column;align-items:center;justify-content:center;gap:6px}
.brand-dot{width:30px;height:30px;border-radius:50%;background:#9aa0aa}
.brand-name{font-size:13px;font-weight:400;letter-spacing:2px;color:#6d727b;text-align:center;line-height:1.15}

/* slider */
.slider{left:243px;top:58px;width:556px;height:176px;border-radius:5px;background:linear-gradient(#151922,#3a3f48 70%,#8f949b);overflow:hidden}
.slide-photo{position:absolute;left:8px;top:10px;width:340px;height:160px;background:radial-gradient(ellipse at 50% 55%,#d8dbe0 0%,#8d929a 35%,rgba(40,44,52,0) 70%)}
.slide-title{position:absolute;left:346px;top:21px;font-size:11px;color:#f0f2f6}
.slide-text{position:absolute;left:346px;top:42px;width:200px;font-size:9.5px;line-height:14px;color:#c9ced8}
.arrow-btn{width:20px;height:20px;border-radius:50%;background:linear-gradient(#fff,#cdd2db);display:flex;align-items:center;justify-content:center}

/* nav */
.nav{left:29px;top:264px;width:781px;height:38px;background:linear-gradient(#505a6c,#2e3644);border-radius:4px;display:flex;box-shadow:0 2px 4px rgba(0,0,0,.5)}
.nav a{display:flex;align-items:center;justify-content:center;font-size:11px;color:#eef0f5;border-right:1px solid #242a35}
.nav a.current{background:linear-gradient(#3d4657,#262d39)}

/* section headings */
.section-head{font-size:13px;font-weight:700;color:var(--head);letter-spacing:.2px}

/* exhibitions */
.exhibit{left:37px;top:346px;width:487px;height:254px;background:var(--lilac)}
.exhibit-photo{position:absolute;left:9px;top:9px;width:289px;height:208px;background:linear-gradient(135deg,#0b1a2a,#1a6fa5 40%,#0c2538 75%,#0a0f18)}
.exhibit-caption{position:absolute;left:9px;top:226px;width:289px;text-align:center;font-size:12px;font-weight:700;color:#4a5578}
.exhibit-text{position:absolute;left:308px;top:24px;width:170px;font-family:Arimo,Arial,sans-serif;font-size:9.6px;line-height:14px;color:var(--lilac-ink);text-align:justify}
.exhibit-meta{position:absolute;left:308px;top:127px;font-family:Arimo,Arial,sans-serif;font-size:9.6px;line-height:15px;font-weight:700;color:var(--lilac-ink)}
.btn-light{position:absolute;left:342px;top:184px;width:93px;height:21px;border-radius:4px;background:linear-gradient(#fff,#dde1ea);box-shadow:0 1px 2px rgba(0,0,0,.35);font-family:Arimo,Arial,sans-serif;font-size:10px;font-weight:700;color:#2c3450;display:flex;align-items:center;justify-content:center}

/* latest products */
.latest{left:550px;top:346px;width:254px;height:254px;background:var(--lilac)}
.latest-photo{position:absolute;left:10px;top:9px;width:235px;height:127px;background:linear-gradient(#6f6a63,#8b5a4a 55%,#5e2f25)}
.latest-rule{position:absolute;left:0;top:150px;width:254px;height:1px;background:#6f7aa3}
.promo-title{position:absolute;top:162px;width:254px;text-align:center;font-size:13px;font-weight:700;color:var(--ink)}
.promo-line{position:absolute;width:254px;text-align:center;font-weight:700;color:#2e3654}
.promo-date{position:absolute;left:28px;top:230px;font-size:10px;color:#3e4664}
.promo-more{position:absolute;left:176px;top:230px;font-size:10px;color:#3e4664;text-decoration:underline}

/* info band */
.info{left:36px;top:621px;width:768px;height:157px;background:var(--panel-dark)}
.col-head{position:absolute;top:24px;width:191px;height:18px;background:#2b303b;font-size:12px;color:#e6e9f0;padding-left:4px;line-height:18px}
.col-rule{position:absolute;top:22px;width:1px;height:110px;background:#262c37}
.news-text{position:absolute;left:20px;top:51px;width:185px;font-size:10.5px;line-height:14px;text-align:justify;color:var(--text-light)}
.read-more{position:absolute;left:156px;top:116px;font-size:10.5px;color:var(--text-light)}
.cat-list{position:absolute;left:277px;top:51px;list-style:none;font-size:10.5px;line-height:21px;color:var(--text-light)}
.cat-list li::before{content:"›";margin-right:6px}
.chat-text{position:absolute;left:550px;top:51px;font-size:10.5px}
.chat-btn{position:absolute;left:549px;top:73px;width:170px;height:47px;border-radius:3px;background:linear-gradient(#f4f6f9,#cfd5de);display:flex;align-items:center;padding-left:22px;gap:12px}
.chat-icon{width:40px;height:36px;background:#b7bdc7;border-radius:3px;display:flex;align-items:center;justify-content:center}
.chat-name{font-size:14px;font-weight:700;color:#4e5563;line-height:16px}
.chat-state{font-size:10px;font-weight:700;color:#4e5563;letter-spacing:.5px}

/* products */
.products-bar{left:36px;top:791px;width:768px;height:31px;background:linear-gradient(#343c4c,#262d3a);display:flex;align-items:center;padding-left:10px}
.card{top:836px;width:144px;height:162px;background:linear-gradient(#ffffff,#e3e6eb);border-radius:3px}
.card-photo{position:absolute;left:6px;top:6px;width:132px;height:86px;background:radial-gradient(ellipse at 50% 40%,#8a6e5d,#1a1412 70%)}
.card-photo.glass{background:linear-gradient(135deg,#1f2b3b,#7d8fa6 50%,#1b2430)}
.card-photo.pale{background:linear-gradient(#f4f5f7,#d8dbe0)}
.ribbon{position:absolute;left:-3px;top:-2px}
.card-model{position:absolute;top:101px;width:144px;text-align:center;font-size:9.5px;color:#222}
.card-rating{position:absolute;top:120px;width:144px;text-align:center;font-size:9.5px;color:#222}
.star{font-size:11px;letter-spacing:-1px}
.star.on{color:#222}.star.off{color:#c0c4cb}
.card-more{position:absolute;left:20px;top:140px;font-size:9.5px;color:#4a5164}
.buy{position:absolute;left:87px;top:138px;width:48px;height:16px;background:#111;border-radius:2px;color:#fff;font-size:8.5px;display:flex;align-items:center;justify-content:center}

/* footer */
.footer{left:0;top:1013px;width:839px;height:138px;background:rgba(14,18,27,.55)}
.foot-head{font-size:10px;font-weight:700;color:#f2f4f8}
.foot-list{list-style:none;font-size:9px;line-height:17.7px;color:#d6dae3}
.foot-list.dots li::before{content:"•";margin-right:5px}
.foot-box{left:564px;width:232px;background:#0f131b;border-radius:2px}
.news-input{position:absolute;left:15px;top:25px;width:138px;height:18px;background:#05070b;border:1px solid #262b35}
.submit{position:absolute;left:160px;top:25px;width:44px;height:16px;border-radius:2px;background:linear-gradient(#fff,#d4d8df);color:#222;font-size:8.5px;display:flex;align-items:center;justify-content:center}
.social{width:24px;height:24px;border-radius:50%}
.legal{left:0;top:1151px;width:839px;height:49px;background:#0c0f16;text-align:center;line-height:52px;font-size:9px;color:#d1d5de}
</style>
</head>
<body>

<!-- top bar -->
<div class="abs lang"><span class="flag" style="background:#2a3f7d;box-shadow:inset 0 0 0 3px #c8102e"></span>English</div>
<div class="abs lang-select">
  <svg class="flag" viewBox="0 0 15 10"><rect width="15" height="10" fill="#c8102e"/><rect x="4" width="2" height="10" fill="#fff"/><rect y="4" width="15" height="2" fill="#fff"/></svg>
  <span>Danish</span>
  <svg width="9" height="6" viewBox="0 0 9 6"><path d="M1 1l3.5 3.5L8 1" stroke="#fff" stroke-width="1.8" fill="none"/></svg>
</div>
<div class="abs toplinks">
  <svg width="14" height="13" viewBox="0 0 14 13"><path d="M7 0L0 6h2v7h4V9h2v4h4V6h2z" fill="#e8ecf4"/></svg>
  <a href="#" style="margin-left:11px">Contact Us</a><span>|</span><a href="#">Login</a>
</div>
<div class="abs search">
  <svg width="14" height="14" viewBox="0 0 14 14"><circle cx="5.5" cy="5.5" r="4.3" stroke="#1c2028" stroke-width="1.8" fill="none"/><path d="M8.5 8.5L13 13" stroke="#1c2028" stroke-width="2.2"/></svg>
  <span>Search</span>
</div>

<!-- brand -->
<div class="abs brand-card">
  <span class="brand-dot"></span>
  <span class="brand-name">VELLMAR<br>GLASSWORKS</span>
</div>

<!-- slider -->
<div class="abs slider">
  <div class="slide-photo" role="img" aria-label="Three clear faceted crystal spheres on a reflective surface"></div>
  <div class="slide-title">Lorem Ipsum Contantry</div>
  <p class="slide-text">Sections 1.10.32 and 1.10.33 from "de Finibus Bonorum et Malorum" by Corvin are also repro-duced in their exact original form.</p>
</div>
<div class="abs arrow-btn" style="left:233px;top:136px"><svg width="8" height="10" viewBox="0 0 8 10"><path d="M6 1L2 5l4 4" stroke="#2f4c8f" stroke-width="2" fill="none"/></svg></div>
<div class="abs arrow-btn" style="left:788px;top:136px"><svg width="8" height="10" viewBox="0 0 8 10"><path d="M2 1l4 4-4 4" stroke="#2f4c8f" stroke-width="2" fill="none"/></svg></div>

<!-- navigation -->
<nav class="abs nav">
  <a href="#" class="current" style="width:77px">Home</a>
  <a href="#" style="width:70px">Facilities</a>
  <a href="#" style="width:97px">Media Center</a>
  <a href="#" style="width:68px">Careers</a>
  <a href="#" style="width:77px">About Us</a>
  <a href="#" style="width:84px">Contact Us</a>
</nav>

<!-- news: exhibitions -->
<h2 class="abs section-head" style="left:37px;top:320px">EXHIBITIONS COVERAGE</h2>
<section class="abs exhibit">
  <div class="exhibit-photo" role="img" aria-label="Exhibition hall with large blue-lit crystal installations"></div>
  <div class="exhibit-caption">Finibus Bonorum et Malorum</div>
  <p class="exhibit-text">Sections 1.10.32 and 1.10.33 from "de Finibus Bonorum et Malorum" by Corvin are also reproduced in their exact original form, accompanied by English versions from the 1914 trans-lation by H. Marlow.</p>
  <div class="exhibit-meta">Model no : 123456<br>Date : Sep, 10, 2011</div>
  <a href="#" class="btn-light">View more...</a>
</section>

<!-- news: latest products -->
<h2 class="abs section-head" style="left:550px;top:320px">LATEST PRODUCTS</h2>
<section class="abs latest">
  <div class="latest-photo" role="img" aria-label="Raw quartz crystal points arranged around a woven ring on a table"></div>
  <div class="latest-rule"></div>
  <div class="promo-title">PROMOTIONAL ANNOUNCEMENTS</div>
  <div class="promo-line" style="top:186px;font-size:11.5px">Sections 1.10.32 and 1.10.33 from</div>
  <div class="promo-line" style="top:206px;font-size:13px">"de Finibus Bonorum et Malorum"</div>
  <div class="promo-date">Date : Sep, 10, 2011</div>
  <a href="#" class="promo-more">View more...</a>
</section>

<!-- info band -->
<section class="abs info">
  <div class="col-head" style="left:16px">Corporate News
    <svg style="position:absolute;right:8px;top:5px" width="16" height="8" viewBox="0 0 16 8"><path d="M4 1L1 4l3 3M12 1l3 3-3 3" stroke="#fff" stroke-width="1.6" fill="none"/></svg>
  </div>
  <p class="news-text">Sections 1.10.32 and 1.10.33 from "de Finibus Bonorum et Malorum" by Corvin are also reproduced in their exact original form.</p>
  <a href="#" class="read-more">Read more</a>
  <div class="col-rule" style="left:242px"></div>
  <div class="col-head" style="left:270px">Categoreies</div>
  <ul class="cat-list">
    <li>Crystal Fashion Components</li>
    <li>Chandeliers Crystal Parts</li>
    <li>Lighting Collection and special design</li>
    <li>Gifts and accessories</li>
  </ul>
  <div class="col-rule" style="left:504px"></div>
  <div class="col-head" style="left:532px">Live Chat</div>
  <div class="chat-text">Live Chat from ChatBrio</div>
  <a href="#" class="chat-btn">
    <span class="chat-icon"><svg width="24" height="20" viewBox="0 0 24 20"><ellipse cx="9" cy="8" rx="8" ry="6" fill="#2f3540"/><ellipse cx="16" cy="12" rx="7" ry="5" fill="#2f3540" stroke="#b7bdc7" stroke-width="1.5"/></svg></span>
    <span><span class="chat-name">CHATBRIO</span><br><span class="chat-state">&gt;&gt;&nbsp; Offline</span></span>
  </a>
</section>

<!-- our products -->
<div class="abs products-bar"><h2 class="section-head">OUR PRODUCTS</h2></div>
<svg class="abs" style="left:763px;top:800px" width="28" height="12" viewBox="0 0 28 12"><path d="M8 1L3 6l5 5M20 1l5 5-5 5" stroke="#d8dcea" stroke-width="2.4" fill="none"/></svg>

<article class="abs card" style="left:36px">
  <div class="card-photo" role="img" aria-label="Crystal necklace worn against a dark background"></div>
  <svg class="ribbon" width="30" height="30" viewBox="0 0 30 30"><path d="M0 14L14 0h12L0 26z" fill="#1aa6d9"/><text x="6" y="17" transform="rotate(-45 10 13)" font-size="7" fill="#fff" font-family="Arial" font-weight="700">NEW</text></svg>
  <div class="card-model">Model Name :&nbsp; Lorem Ipsum</div>
  <div class="card-rating">Rating : <span class="star on">★◐</span><span class="star off">☆☆☆</span></div>
  <a href="#" class="card-more">View More</a><a href="#" class="buy">BUY THIS</a>
</article>
<article class="abs card" style="left:192px">
  <div class="card-photo" role="img" aria-label="Fine crystal pendant necklace on a dark background"></div>
  <svg class="ribbon" width="30" height="30" viewBox="0 0 30 30"><path d="M0 14L14 0h12L0 26z" fill="#1aa6d9"/><text x="6" y="17" transform="rotate(-45 10 13)" font-size="7" fill="#fff" font-family="Arial" font-weight="700">NEW</text></svg>
  <div class="card-model">Model Name :&nbsp; Lorem Ipsum</div>
  <div class="card-rating">Rating : <span class="star on">★◐</span><span class="star off">☆☆☆</span></div>
  <a href="#" class="card-more">View More</a><a href="#" class="buy">BUY THIS</a>
</article>
<article class="abs card" style="left:347px">
  <div class="card-photo" role="img" aria-label="Crystal collar necklace with drop strands"></div>
  <div class="card-model">Model Name :&nbsp; Lorem Ipsum</div>
  <div class="card-rating">Rating : <span class="star on">★◐</span><span class="star off">☆☆☆</span></div>
  <a href="#" class="card-more">View More</a><a href="#" class="buy">BUY THIS</a>
</article>
<article class="abs card" style="left:504px">
  <div class="card-photo glass" role="img" aria-label="Clear crystal swan figurine"></div>
  <div class="card-model">Model Name :&nbsp; Lorem Ipsum</div>
  <div class="card-rating">Rating : <span class="star on">★◐</span><span class="star off">☆☆☆</span></div>
  <a href="#" class="card-more">View More</a><a href="#" class="buy">BUY THIS</a>
</article>
<article class="abs card" style="left:660px">
  <div class="card-photo pale" role="img" aria-label="Crystal-set curved pendant on a light background"></div>
  <div class="card-model">Model Name :&nbsp; Lorem Ipsum</div>
  <div class="card-rating">Rating : <span class="star on">★◐</span><span class="star off">☆☆☆</span></div>
  <a href="#" class="card-more">View More</a><a href="#" class="buy">BUY THIS</a>
</article>

<!-- footer -->
<footer class="abs footer"></footer>
<h3 class="abs foot-head" style="left:71px;top:1025px">Other Websites</h3>
<ul class="abs foot-list" style="left:62px;top:1045px">
  <li>www.vellmarglass.com</li><li>www.vellmarglass.com</li><li>www.vellmarglass.com</li><li>www.vellmarglass.com</li><li>www.vellmarglass.com</li>
</ul>
<h3 class="abs foot-head" style="left:215px;top:1025px">About Us</h3>
<ul class="abs foot-list dots" style="left:214px;top:1045px">
  <li>Company Info</li><li>Our Prtoducts</li><li>Shipping</li><li>Privacy Policy</li><li>Terms and Conditions</li>
</ul>
<h3 class="abs foot-head" style="left:347px;top:1026px">Advice</h3>
<ul class="abs foot-list dots" style="left:346px;top:1046px">
  <li>FAQs</li><li>Solutions</li><li>Contacts</li><li>Customer Care</li><li>Free Phones</li>
</ul>
<h3 class="abs foot-head" style="left:451px;top:1026px">Join in</h3>
<ul class="abs foot-list dots" style="left:450px;top:1046px">
  <li>Sign up</li><li>Log in</li><li>Forums</li><li>Promotions</li><li>Sitemap</li>
</ul>

<div class="abs foot-box" style="top:1021px;height:54px">
  <h3 class="foot-head" style="position:absolute;left:7px;top:6px">NEWS LETTER</h3>
  <div class="news-input"></div>
  <a href="#" class="submit">SUBMIT</a>
</div>
<div class="abs foot-box" style="top:1082px;height:51px;display:flex;align-items:center;padding-left:7px;gap:6px">
  <h3 class="foot-head" style="margin-right:14px">Connect With US :</h3>
  <span class="social" style="background:#4a66a8"></span>
  <span class="social" style="background:#3fb6e6"></span>
  <span class="social" style="background:#f08a1c"></span>
  <span class="social" style="background:#eef0f3"></span>
</div>

<div class="abs legal">Copyright @ 2011 www.vellmarglass.com All rights reserved</div>

</body>
</html>
```